Business Card Design Project - Nerd Crew

High quality business card Must be funky.

We are an IT support from home and office, but our image is more retro.

Our logo is black and lime green. IT should be a 2 sided card with the multiple coloured ties somehow used on the reverse side (be creative!)

Black or white background fine or a combo of both

Target Market(s)

consumer and business

Industry/Entity Type

Business

```html
<!DOCTYPE html>
<html lang="en">
<head>
<meta charset="utf-8">
<title>Nerd Crew – Business Card</title>
<link rel="stylesheet" href="https://fonts.googleapis.com/css2?family=Cabin:wght@400;500;600&display=swap">
<style>
  :root {
    --stage: #2a2a2a;
    --card-white: #f4f4f4;
    --card-black: #1c1a1c;
    --ink: #1d1d1d;
    --lime: #8cc63f;
    --tie-yellow: #f2e21d;
    --tie-pink: #e9407a;
    --tie-cyan: #11b3cf;
    --tie-red: #e3202f;
    --tie-lime: #8dc63f;
  }
  * { margin: 0; padding: 0; box-sizing: border-box; }
  html, body { width: 1200px; height: 901px; overflow: hidden; }
  body {
    background: var(--stage);
    font-family: "Cabin", "Gill Sans", sans-serif;
    display: flex;
    align-items: center;
    justify-content: center;
    gap: 44px;
  }
  .card {
    width: 520px;
    height: 298px;
    border-radius: 22px;
    position: relative;
    overflow: hidden;
  }
  .card--front { background: var(--card-white); color: var(--ink); }
  .card--back { background: var(--card-black); }

  .brand {
    position: absolute;
    left: 40px;
    top: 42px;
    display: flex;
    align-items: center;
    gap: 12px;
  }
  .brand__mark {
    width: 16px; height: 16px;
    background: var(--lime);
    border-radius: 50%;
  }
  .brand__name {
    font-size: 46px;
    font-weight: 600;
    color: var(--ink);
    letter-spacing: -0.5px;
  }

  .person { position: absolute; left: 40px; top: 158px; }
  .person__name { font-size: 19px; color: var(--lime); letter-spacing: 0.5px; line-height: 1.1; }
  .person__role { font-size: 14px; color: var(--ink); margin-top: 2px; }

  .contact {
    position: absolute; left: 40px; top: 212px;
    display: grid;
    grid-template-columns: 62px auto;
    row-gap: 2px;
    font-size: 14px;
    line-height: 1.25;
  }
  .contact__label { color: var(--lime); }
  .contact__value { color: var(--ink); }

  .website {
    position: absolute; right: 36px; top: 176px;
    font-size: 15px; color: var(--lime);
  }

  .tie-row {
    position: absolute;
    left: 40px; right: 40px;
    top: 112px; height: 74px;
    border-radius: 8px;
    background: linear-gradient(90deg,
      var(--tie-yellow) 0%, var(--tie-pink) 25%, var(--tie-cyan) 48%,
      var(--tie-red) 70%, var(--tie-lime) 100%);
  }
</style>
</head>
<body>
  <section class="card card--front" aria-label="Business card front">
    <div class="brand">
      <span class="brand__name">Nerd Crew</span>
      <span class="brand__mark"></span>
    </div>
    <div class="person">
      <p class="person__name">MARTIN KOLBE</p>
      <p class="person__role">Managing Director</p>
    </div>
    <div class="contact">
      <span class="contact__label">Hotline</span><span class="contact__value">5550 123 456</span>
      <span class="contact__label">Mobile</span><span class="contact__value">8880 246 135</span>
      <span class="contact__label">Email</span><span class="contact__value">info@nerdcrew.asia</span>
    </div>
    <p class="website">www.nerdcrew.asia</p>
  </section>

  <section class="card card--back" aria-label="Business card back">
    <div class="tie-row" role="img" aria-label="Row of multicoloured neckties: yellow, pink, cyan, red, lime striped and lime dotted"></div>
  </section>
</body>
</html>
```